Business card for Parent company and Brands

We're looking for a business card that displays the parent company on one side "KestrelWorks" and shows the brands on the back. Previously I have had a business card for each product range but this is just messy. I put together a mock up version below, just not sure how best to display contact information for each brand and how to best layout the logos.
Key contact details are as follows:

Liam Corwen
Sales Director
(09) 417 6200
0274961153
liam@kestrelworks.co.nz
www.kestrelworks.co.nz - currently parked

Target Market(s)

Professionals e.g. Businesses, Schools, Local Government

Industry/Entity Type

Business

Contact Information for Business Card

One side:
KestrelWorks logo
contact details

side two
brands and URL's

Font styles to use
Serif
Sans Serif

Requirements
Must have
• Print ready

```html
<!DOCTYPE html>
<html lang="en">
<head>
<meta charset="utf-8">
<title>KestrelWorks business card</title>
<link href="https://fonts.googleapis.com/css2?family=Arimo:wght@400;700&display=swap" rel="stylesheet">
<style>
  :root {
    --bg: #2b2b2d;
    --paper: #f7f7f7;
    --ink: #1d1d1f;
    --blue: #1f5ba8;
    --blue-dark: #174a8c;
    --grey: #555;
    --orange: #f08a24;
    --red: #c4262e;
  }
  * { margin: 0; padding: 0; box-sizing: border-box; }
  html, body { width: 1200px; height: 997px; overflow: hidden; }
  body { background: var(--bg); font-family: "Arimo", Arial, sans-serif; position: relative; }

  .card {
    position: absolute;
    width: 620px; height: 354px;
    background: var(--paper);
    box-shadow: 0 10px 30px rgba(0,0,0,.45);
    overflow: hidden;
  }
  .card-back { left: 150px; top: 80px; }
  .card-front { left: 430px; top: 500px; }

  /* brand side */
  .brand {
    position: absolute;
    display: flex; align-items: center; gap: 12px;
    font-weight: 700; color: var(--ink); letter-spacing: .5px;
  }
  .brand-mark { width: 26px; height: 26px; flex: none; }
  .brand-stagecraft { left: 60px; top: 70px; font-size: 24px; }
  .brand-stagecraft .brand-mark { background: var(--orange); }
  .brand-corral { left: 390px; top: 40px; font-size: 22px; }
  .brand-corral .brand-mark { background: var(--ink); }
  .brand-parent { left: 215px; top: 150px; font-size: 28px; }
  .brand-parent .brand-mark { background: var(--blue); width: 34px; height: 34px; }
  .brand-tourline { left: 40px; top: 250px; font-size: 22px; }
  .brand-tourline .brand-mark { background: var(--red); border-radius: 50%; }
  .brand-harbour { left: 300px; top: 250px; font-size: 30px; }
  .brand-harbour .brand-mark { background: var(--ink); width: 34px; height: 34px; }

  /* contact side */
  .front-logo {
    position: absolute; left: 190px; top: 42px;
    display: flex; align-items: center; gap: 16px;
    font-size: 40px; font-weight: 700; color: var(--ink); letter-spacing: 2px;
  }
  .front-logo .brand-mark { width: 48px; height: 48px; background: var(--blue); }
  .divider { position: absolute; left: 235px; top: 150px; width: 360px; height: 1.5px; background: var(--blue); }
  .person { position: absolute; left: 34px; top: 166px; }
  .person-name { font-size: 19px; font-weight: 700; color: var(--blue); letter-spacing: .5px; }
  .person-title { font-size: 14px; color: var(--ink); margin-top: 2px; }
  .company { position: absolute; right: 30px; top: 112px; text-align: right; font-size: 14px; color: var(--ink); line-height: 1.3; }
  .company-name { font-size: 15px; font-weight: 700; color: var(--blue); letter-spacing: .5px; }
  .contacts { position: absolute; left: 34px; top: 236px; list-style: none; }
  .contacts li { display: flex; align-items: center; gap: 12px; font-size: 16px; color: var(--ink); height: 26px; }
  .contacts svg { width: 18px; height: 18px; flex: none; }
  .footer-band { position: absolute; left: 0; top: 0; width: 620px; height: 354px; }
  .web { position: absolute; right: 30px; top: 298px; font-size: 15px; font-weight: 700; color: #fff; letter-spacing: 1px; }
</style>
</head>
<body>

<section class="card card-back" aria-label="Brands side">
  <div class="brand brand-stagecraft"><span class="brand-mark"></span>STAGECRAFT SUPPLY</div>
  <div class="brand brand-corral"><span class="brand-mark"></span>Corral Posts</div>
  <div class="brand brand-parent"><span class="brand-mark"></span>KESTRELWORKS</div>
  <div class="brand brand-tourline"><span class="brand-mark"></span>TOURLINE CASES</div>
  <div class="brand brand-harbour"><span class="brand-mark"></span>HARBOURLINE</div>
</section>

<section class="card card-front" aria-label="Contact side">
  <svg class="footer-band" viewBox="0 0 620 354" aria-hidden="true">
    <path d="M0,322 L350,322 Q362,322 366,312 L368,306 L372,306 L370,316 Q364,330 350,330 L0,330 Z" fill="var(--ink)"/>
    <path d="M0,338 L360,338 Q376,338 382,322 L392,296 Q398,282 414,282 L620,282 L620,354 L0,354 Z" fill="var(--blue)"/>
  </svg>

  <div class="front-logo"><span class="brand-mark"></span>KESTRELWORKS</div>
  <div class="divider"></div>

  <div class="person">
    <div class="person-name">LIAM CORWEN</div>
    <div class="person-title">Sales Director</div>
  </div>

  <address class="company" style="font-style:normal">
    <div class="company-name">KESTRELWORKS PVT LTD</div>
    <div>112 Marlow Rd, Ste 4</div>
    <div>Riverton, Auckland</div>
  </address>

  <ul class="contacts">
    <li>
      <svg viewBox="0 0 18 18" aria-hidden="true"><circle cx="9" cy="9" r="9" fill="var(--blue)"/><path d="M5 6 Q5 5 6 5 L12 5 Q13 5 13 6 L13 7 L11 7 L11 6 L7 6 L7 7 L5 7 Z M6 8 L12 8 L13 13 L5 13 Z" fill="#fff"/></svg>
      (09) 417 6200
    </li>
    <li>
      <svg viewBox="0 0 18 18" aria-hidden="true"><circle cx="9" cy="9" r="9" fill="var(--blue)"/><rect x="6.5" y="4" width="5" height="10" rx="1" fill="#fff"/><rect x="7.3" y="5" width="3.4" height="6" fill="var(--blue)"/></svg>
      0274961153
    </li>
    <li>
      <svg viewBox="0 0 18 18" aria-hidden="true"><circle cx="9" cy="9" r="9" fill="var(--blue)"/><rect x="4.5" y="6" width="9" height="6.5" fill="#fff"/><path d="M4.5 6 L9 9.5 L13.5 6" fill="none" stroke="var(--blue)" stroke-width="1"/></svg>
      liam@kestrelworks.co.nz
    </li>
  </ul>

  <div class="web">www.kestrelworks.co.nz</div>
</section>

</body>
</html>
```